"Landing Page Design for Premium Eco-Friendly Laundry Strips – Plooifris.nl"

We need a visually appealing and high-converting landing page for our premium laundry strips, emphasizing luxury, sustainability, and ease of use. The page should include sections such as:

Hero Section: A compelling introduction with a strong headline, subheadline, and a clear call-to-action (CTA).
Product Benefits: Highlighting key features like eco-friendliness, long-lasting scent, and hypoallergenic qualities.
Product Description: Focusing on innovation and sustainability.
How It Works: Simple, visual steps for using the product.
Customer Reviews: Authentic testimonials to build trust and social proof.
FAQ Section: Addressing common concerns about the product.
The design should maintain a luxurious aesthetic while ensuring clarity and user-friendliness. We also offer free shipping on all orders, a key differentiator to be prominently displayed. All texts and translations are already provided for implementation. Please deliver the design in Figma format."

Target Market(s)

"Eco-conscious consumers and families seeking premium and sustainable laundry solutions. Target age group: 25-50, predominantly women who prioritize luxury and environmental impact."

Industry/Entity Type

"Laundry care and eco-friendly consumer goods."

Coding

Requirements
Must have
• A visually luxurious design emphasizing premium quality and eco-friendliness. Clear call-to-actions (e.g., 'Try Now – Free Shipping'). Sections for product benefits, how it works, customer reviews, and FAQ. Highlight free shipping with no minimum order prominently."
Nice to have
• Elegant, minimalist animations to enhance the premium feel. Subtle use of gold and black to emphasize luxury, with a touch of green for sustainability. Interactive customer reviews section (e.g., carousel or testimonials)."
Should not have
• Overly cluttered designs or overwhelming text blocks. Generic stock photos not aligned with our brand identity. Bright or overly playful color schemes that detract from the premium feel."

```html
<!DOCTYPE html>
<html lang="nl">
<head>
<meta charset="utf-8">
<title>Plooifris – Premium Wasstrips</title>
<link href="https://fonts.googleapis.com/css2?family=Roboto:ital,wght@0,300;0,400;0,500;0,700;1,400&display=swap" rel="stylesheet">
<style>
:root{
  --black:#0b0b0b;
  --dark:#1b1b1b;
  --card-dark:#1e1e1e;
  --gold:#d4a537;
  --gold-light:#e9c25a;
  --gold-deep:#b78622;
  --cream:#fcf5e6;
  --green:#3f9a3a;
  --text:#1a1a1a;
  --muted:#555;
  --white:#fff;
}
*{margin:0;padding:0;box-sizing:border-box}
html,body{width:1200px;height:4025px;overflow:hidden}
body{font-family:"Roboto",Arial,sans-serif;color:var(--text);background:var(--white);position:relative}
section,header,footer{position:absolute;left:0;width:1200px;overflow:hidden}
.abs{position:absolute}
.gold{color:var(--gold)}
.label{font-size:14px;color:var(--green);letter-spacing:.5px;text-transform:uppercase}
.heading{font-size:35px;font-weight:400;line-height:1.2}
.heading .u{display:inline-block;border-bottom:3px solid var(--gold);padding-bottom:4px}
.note{font-size:10px;color:#444}
.btn-gold{background:linear-gradient(180deg,var(--gold-light),var(--gold-deep));color:#1a1a1a;border-radius:6px;display:flex;align-items:center;justify-content:center;font-size:17px}
.btn-outline{border:1.5px solid var(--gold);border-radius:6px;display:flex;align-items:center;justify-content:center;font-size:17px;background:#fff}
.photo{position:absolute}
.center{text-align:center;left:0;width:1200px}

/* header */
.site-header{top:0;height:112px;background:var(--black)}
.brand{left:39px;top:22px;width:72px;text-align:center;color:var(--gold);font-size:10px;letter-spacing:1px}
.brand .mark{width:34px;height:34px;border:2px solid var(--gold);border-radius:50%;margin:0 auto 6px}
.announce{left:195px;top:38px;font-size:23px;color:var(--gold)}
.announce b{font-weight:700}
.header-btn{left:1028px;top:34px;width:134px;height:36px;border:1.5px solid var(--gold);border-radius:5px;color:#fff;font-size:16px;display:flex;align-items:center;justify-content:center}

/* hero */
.hero{top:112px;height:560px;background:radial-gradient(ellipse at 70% 40%,#3a3a3a 0%,#1a1a1a 55%,#111 100%)}
.hero-title{left:60px;top:108px;font-size:46px;font-weight:700;color:#fff;line-height:1.15;letter-spacing:.5px}
.hero-sub{left:60px;top:238px;width:480px;font-size:15px;color:#ddd;letter-spacing:1px;line-height:1.25}
.hero-btn{left:60px;top:325px;width:326px;height:52px;font-size:17px}
.hero-note{left:60px;top:388px;color:#ccc;font-size:10px}
.pay{left:60px;top:404px;display:flex;gap:8px}
.pay span{width:25px;height:18px;border-radius:3px;background:#fff}
.hero-photo{left:790px;top:45px;width:410px;height:460px;background:linear-gradient(160deg,#f3efe6 0%,#d4a537 30%,#111 55%,#2a3a1e 100%);border-radius:4px}
.hero-wave{left:0;bottom:0;width:1200px;height:120px}

/* benefits */
.benefits{top:672px;height:578px;background:#fff}
.benefits .label{left:60px;top:56px}
.benefits .heading{left:60px;top:78px;width:280px}
.benefits .btn-outline{left:60px;top:322px;width:199px;height:51px}
.benefits .note{left:60px;top:384px}
.card{position:absolute;width:239px;height:218px;background:var(--cream);border-radius:12px;text-align:center;padding:18px 20px 0}
.card svg{width:50px;height:50px;display:block;margin:0 auto 14px}
.card h3{font-size:15px;font-weight:400;line-height:1.5;display:inline-block;padding-bottom:6px;border-bottom:2px solid var(--green)}
.card p{font-size:12.5px;color:#444;line-height:1.35;margin-top:14px}

/* description */
.desc{top:1250px;height:490px}
.desc-left{left:0;top:0;width:669px;height:490px;background:var(--cream)}
.desc .label{left:60px;top:56px}
.desc .heading{left:60px;top:82px}
.desc-text{left:60px;top:200px;width:480px;font-size:12.5px;line-height:26px;color:#333}
.desc .btn-outline{left:60px;top:361px;width:186px;height:52px;background:transparent}
.desc .note{left:68px;top:423px}
.desc-photo{left:669px;top:0;width:531px;height:490px;background:radial-gradient(ellipse at 55% 50%,#d4a537 0%,#1c1c1c 45%,#2d2d2d 100%)}

/* how it works */
.how{top:1740px;height:573px;background:#fff}
.how .label{top:48px;font-size:13px}
.how .heading{top:72px}
.step{position:absolute;top:155px;width:256px;height:261px;background:#fff;border-radius:26px;box-shadow:0 4px 10px rgba(212,165,55,.35),0 -3px 0 var(--gold-light);text-align:center}
.step .pic{position:absolute;left:19px;top:24px;width:219px;height:117px}
.step .num{position:absolute;left:114px;top:172px;width:28px;height:28px;border-radius:50%;background:var(--gold);color:#111;font-size:13px;display:flex;align-items:center;justify-content:center;font-weight:500}
.step p{position:absolute;left:18px;top:212px;width:220px;font-size:12.5px;color:#444;line-height:1.35}
.how .btn-gold{left:470px;top:455px;width:258px;height:52px;font-size:16px}
.how .note{top:520px}

/* reviews */
.reviews{top:2313px;height:515px;background:var(--black)}
.reviews .label{top:50px;font-size:13px}
.reviews .heading{top:84px;color:#fff}
.review{position:absolute;top:181px;width:415px;height:244px;background:var(--card-dark);border-radius:12px;text-align:center}
.review .q{margin:22px auto 0;width:60px;height:44px}
.review p{margin-top:22px;font-size:16px;font-style:italic;color:#ccc;line-height:1.4;padding:0 60px}
.review hr{border:0;border-top:1.5px solid var(--green);width:190px;margin:18px auto 0}
.review .who{margin-top:18px;display:flex;align-items:center;justify-content:center;gap:10px;color:#bbb;font-size:12px}
.review .who span.av{width:28px;height:28px;border-radius:50%;background:linear-gradient(#e6e0d6,#9a8f80)}
.arrow{position:absolute;top:292px;width:28px;height:28px;border-radius:50%;background:var(--gold);display:flex;align-items:center;justify-content:center}
.dots{top:456px;left:535px;display:flex;gap:18px}
.dots span{width:16px;height:16px;border-radius:50%;border:2px solid var(--gold)}
.dots span.on{background:var(--gold)}

/* faq */
.faq{top:2828px;height:562px;background:#fff}
.faq .label{top:48px;font-size:13px}
.faq .heading{top:82px}
.faq-item{position:absolute;left:216px;width:768px;border-bottom:1.5px solid #555}
.faq-item h4{font-size:16px;font-weight:400}
.faq-item p{font-size:12.5px;color:#555;margin-top:18px}
.faq-item .x{position:absolute;right:8px;top:0;width:22px;height:22px}
.faq-box{left:216px;top:438px;width:768px;height:76px;border:1.5px solid #e6e6e6;border-radius:6px}
.faq-box .small{position:absolute;left:126px;top:30px;font-size:12px;color:#555}
.faq-box .btn-outline{position:absolute;left:279px;top:10px;width:361px;height:52px;font-size:16px}

/* final cta */
.final{top:3390px;height:540px;background:#161616}
.final-wave{left:0;top:0;width:1200px;height:100px}
.final-photo{left:86px;top:79px;width:430px;height:445px;background:linear-gradient(160deg,#f3efe6 0%,#d4a537 30%,#111 58%,#2a3a1e 100%);border-radius:4px}
.final .brand{left:559px;top:102px;text-align:left;width:120px}
.final .brand .mark{margin:0 0 6px 12px}
.final-title{left:559px;top:199px;width:560px;font-size:33px;color:#fff;line-height:1.2;font-weight:400}
.final .btn-gold{left:559px;top:376px;width:296px;height:50px;font-size:16px}
.final .note{left:603px;top:440px;color:#ccc}

.site-footer{top:3930px;height:95px;background:var(--black);color:#ddd;font-size:12.5px;text-align:center;padding-top:41px}
</style>
</head>
<body>

<header class="site-header">
  <div class="abs brand"><div class="mark"></div>PLOOIFRIS</div>
  <div class="abs announce"><b>*Gratis Verzending</b> op <b>Alle Bestellingen</b>: Geen Minimum Bestelbedrag</div>
  <div class="abs header-btn">Bestel Nu</div>
</header>

<section class="hero">
  <h1 class="abs hero-title">Ervaar <span class="gold">Luxe</span> en <span class="gold">Duurzaamheid</span><br>in Elke Wasbeurt</h1>
  <p class="abs hero-sub">Ontdek de premium wasstrips van Plooifris – waar verfijning en ecologisch bewustzijn samenkomen.</p>
  <div class="abs btn-gold hero-btn">Probeer Nu – Altijd Gratis Verzending!</div>
  <div class="abs hero-note">*Gratis Verzending zonder Minimale Bestelling smells</div>
  <div class="abs pay"><span></span><span></span><span></span><span></span><span></span></div>
  <div class="photo hero-photo" role="img" aria-label="Verpakking Plooifris wasstrips, zwart met goud, tussen palmbladeren"></div>
  <svg class="abs hero-wave" viewBox="0 0 1200 120" preserveAspectRatio="none">
    <path d="M0 50 C250 75 450 120 700 100 S1050 40 1200 30 L1200 120 L0 120Z" fill="#fff"/>
    <path d="M0 50 C250 75 450 120 700 100 S1050 40 1200 30" fill="none" stroke="#d4a537" stroke-width="9"/>
  </svg>
</section>

<section class="benefits">
  <div class="abs label">Productvoordelen</div>
  <h2 class="abs heading">Waarom Kiezen Voor Plooifris <span class="u">Wasstrips?</span></h2>
  <div class="abs btn-outline">Probeer Nu</div>
  <div class="abs note">*Gratis Verzending zonder Minimale Bestelling</div>

  <div class="card" style="left:380px;top:81px">
    <svg viewBox="0 0 50 50"><path d="M25 44V22M25 30c-8 0-14-5-14-12 8 0 14 5 14 12zM25 24c0-8 6-13 14-13 0 7-6 13-14 13z" fill="#d4a537"/></svg>
    <h3>Milieuvriendelijk</h3>
    <p>100% biologisch afbreekbaar en plasticvrij.</p>
  </div>
  <div class="card" style="left:638px;top:81px">
    <svg viewBox="0 0 50 50"><path d="M17 8l-11 8 5 8 4-3v23h20V21l4 3 5-8-11-8c-1 4-4 6-8 6s-7-2-8-6z" fill="#d4a537"/></svg>
    <h3>Geschikt voor<br>Alle Stoffen</h3>
    <p>Veilig voor fijne was, wit, kleur en zwart.</p>
  </div>
  <div class="card" style="left:895px;top:81px">
    <svg viewBox="0 0 50 50"><path d="M14 26l12 16 14-14-6-6-6 6-8-10z" fill="#d4a537"/><path d="M22 8v6M30 6v6M38 10l-3 5" stroke="#d4a537" stroke-width="2.5"/></svg>
    <h3>Compact en<br>Gebruiksvriendelijk</h3>
    <p>Geen gedoe met zware flessen – scheur, voeg toe en geniet.</p>
  </div>
  <div class="card" style="left:380px;top:317px">
    <svg viewBox="0 0 50 50"><g fill="#d4a537"><circle cx="25" cy="14" r="8"/><circle cx="36" cy="23" r="8"/><circle cx="32" cy="36" r="8"/><circle cx="18" cy="36" r="8"/><circle cx="14" cy="23" r="8"/></g><circle cx="25" cy="26" r="5" fill="#fcf5e6"/></svg>
    <h3>Langdurige Geur</h3>
    <p>Een heerlijke frisse geur die dagenlang blijft hangen.</p>
  </div>
  <div class="card" style="left:638px;top:317px">
    <svg viewBox="0 0 50 50"><path d="M12 40c-4-6-2-14 4-20l8-8 3 3-6 7 10-9 3 3-9 9 10-7 3 3-11 10 8-5 2 3-12 10c-5 4-10 4-13 1z" fill="#d4a537"/></svg>
    <h3>Hypoallergeen</h3>
    <p>Perfect voor de gevoelige huid en babykleding.</p>
  </div>
  <div class="card" style="left:895px;top:317px">
    <svg viewBox="0 0 50 50"><path d="M5 14h26v20H5zM31 20h8l6 7v7H31z" fill="#d4a537"/><circle cx="13" cy="36" r="4" fill="#d4a537" stroke="#fcf5e6" stroke-width="2"/><circle cx="37" cy="36" r="4" fill="#d4a537" stroke="#fcf5e6" stroke-width="2"/></svg>
    <h3>Altijd Gratis<br>Verzending</h3>
    <p>Geen minimale bestelhoeveelheid vereist.</p>
  </div>
</section>

<section class="desc">
  <div class="abs desc-left"></div>
  <div class="abs label">Productbeschrijving</div>
  <h2 class="abs heading">The Future of<br><span class="u">Laundry Is Here</span></h2>
  <p class="abs desc-text">Onze Plooifris Wasstrips combineren innovatie met duurzaamheid. Met slechts één strip per wasbeurt geniet je van een schone en heerlijk geurende was, zonder het milieu te belasten. Geen plastic flessen, geen verspilling – alleen pure waskracht in een handige strip.</p>
  <div class="abs btn-outline">Bestel Nu</div>
  <div class="abs note">*Free Shipping with No Minimum order</div>
  <div class="photo desc-photo" role="img" aria-label="Verpakking Plooifris wasstrips op donkere achtergrond"></div>
</section>

<section class="how">
  <div class="abs center label">Hoe het werkt</div>
  <h2 class="abs center heading">Zo Gebruik Je <span class="u">Wasstrips</span></h2>
  <div class="step" style="left:60px"><div class="pic" role="img" aria-label="Handen die een wasstrip afscheuren" style="background:linear-gradient(90deg,#4a6fa3,#f2f2f2 40%,#e8e8e8 60%,#7ea0c8)"></div><div class="num">1</div><p>Scheur een wasstrip af.</p></div>
  <div class="step" style="left:334px"><div class="pic" role="img" aria-label="Wasstrip bij wasgoed in de trommel" style="background:linear-gradient(135deg,#2f6f7a,#5b9aa3 50%,#2d4c55)"></div><div class="num">2</div><p>Plaats de strip direct in de trommel, samen met je wasgoed.</p></div>
  <div class="step" style="left:609px"><div class="pic" role="img" aria-label="Hand die de wasmachine start" style="background:linear-gradient(135deg,#e6e6e6,#9a9a9a 55%,#2b2b2b)"></div><div class="num">3</div><p>Start de wasmachine en laat de wasstrip zijn werk doen.</p></div>
  <div class="step" style="left:884px"><div class="pic" role="img" aria-label="Persoon met schone, fris ruikende handdoeken" style="background:linear-gradient(90deg,#f4f4f6,#e7e7ea 50%,#a8c7cf)"></div><div class="num">4</div><p>Geniet van perfect schone en fris ruikende kleding!</p></div>
  <div class="abs btn-gold">Shop Nu – Vanaf <b>&nbsp;€14,95</b></div>
  <div class="abs center note">*Gratis Verzending zonder Minimale Bestelling</div>
</section>

<section class="reviews">
  <div class="abs center label">Klantbeoordelingen</div>
  <h2 class="abs center heading"><span class="u">Wat Onze Klanten Zeggen</span></h2>
  <div class="arrow" style="left:140px"><svg width="12" height="12" viewBox="0 0 12 12"><path d="M8 1L3 6l5 5" fill="none" stroke="#111" stroke-width="2"/></svg></div>
  <div class="review" style="left:166px">
    <svg class="q" viewBox="0 0 60 44"><g fill="#d4a537"><circle cx="14" cy="28" r="13"/><path d="M2 28C2 12 10 4 22 2l2 5C14 10 12 18 12 28z"/><circle cx="44" cy="28" r="13"/><path d="M32 28C32 12 40 4 52 2l2 5C44 10 42 18 42 28z"/></g></svg>
    <p>Sinds ik Plooifris gebruik, voelt mijn was frisser en luxueuzer aan dan ooit.</p>
    <hr>
    <div class="who"><span class="av"></span>- Sophie</div>
  </div>
  <div class="review" style="left:619px">
    <svg class="q" viewBox="0 0 60 44"><g fill="#d4a537"><circle cx="14" cy="28" r="13"/><path d="M2 28C2 12 10 4 22 2l2 5C14 10 12 18 12 28z"/><circle cx="44" cy="28" r="13"/><path d="M32 28C32 12 40 4 52 2l2 5C44 10 42 18 42 28z"/></g></svg>
    <p>Eindelijk een milieuvriendelijk product dat echt werkt en heerlijk ruikt.</p>
    <hr>
    <div class="who"><span class="av"></span>- Mark</div>
  </div>
  <div class="arrow" style="left:1027px"><svg width="12" height="12" viewBox="0 0 12 12"><path d="M4 1l5 5-5 5" fill="none" stroke="#111" stroke-width="2"/></svg></div>
  <div class="abs dots"><span class="on"></span><span></span><span></span><span></span></div>
</section>

<section class="faq">
  <div class="abs center label">FAQ-sectie</div>
  <h2 class="abs center heading">Heb Je Nog <span class="u">Vragen?</span></h2>
  <div class="faq-item" style="top:164px;height:78px">
    <h4>Zijn de wasstrips geschikt voor mensen met een gevoelige huid?</h4>
    <p>Ja, onze wasstrips zijn hypoallergeen en dermatologisch getest, waardoor ze veilig zijn voor de gevoelige huid.</p>
    <svg class="x" viewBox="0 0 22 22"><path d="M2 2l18 18M20 2L2 20" stroke="#222" stroke-width="2"/></svg>
  </div>
  <div class="faq-item" style="top:260px;height:78px">
    <h4>Hoeveel wasbeurten bevat één verpakking?</h4>
    <p>Elke verpakking bevat 30 strips, goed voor 30 wasbeurten.</p>
    <svg class="x" viewBox="0 0 22 22"><path d="M2 2l18 18M20 2L2 20" stroke="#222" stroke-width="2"/></svg>
  </div>
  <div class="faq-item" style="top:376px;height:29px">
    <h4 style="margin-top:10px">Werken de strips bij lage temperaturen?</h4>
    <svg class="x" viewBox="0 0 22 22" style="top:0"><path d="M11 0v22M0 11h22" stroke="#d4a537" stroke-width="2"/></svg>
  </div>
  <div class="abs faq-box">
    <span class="small">Still have questions?</span>
    <div class="btn-outline">Bekijk Onze FAQ Voor Meer Antwoorden</div>
  </div>
</section>

<section class="final">
  <svg class="abs final-wave" viewBox="0 0 1200 100" preserveAspectRatio="none">
    <path d="M0 0H1200V55C1000 80 850 60 650 40S250 20 0 70Z" fill="#fff"/>
    <path d="M0 70C250 20 450 20 650 40S1000 80 1200 55" fill="none" stroke="#d4a537" stroke-width="9"/>
  </svg>
  <div class="photo final-photo" role="img" aria-label="Verpakking Plooifris wasstrips tussen palmbladeren"></div>
  <div class="abs brand"><div class="mark"></div>PLOOIFRIS</div>
  <h2 class="abs final-title">Start Vandaag Met Milieuvriendelijk Wassen – Geen Plastic, Geen Gedoe. Alleen Fris Wassen.</h2>
  <div class="abs btn-gold">Bestel Nu – Maak Het Verschil!</div>
  <div class="abs note">*Gratis Verzending zonder Minimale Bestelling</div>
</section>

<footer class="site-footer">Alle rechten voorbehouden © 2024 Plooifris</footer>

</body>
</html>
```